VORELLI Industrial Maintenance

I offer repair and maintenance services of industrial mechanics in Quebec. I would like a creation that reflects confidence, competence, professionalism and dynamism. I like the orange color and the blue color.

Target Market(s)

Industries and Manufacturing companies using industrial machinery for the manufacture of their products.

Industry/Entity Type

Manufacturing

Contact Information for Business Card

VORELLI Maintenance Industrielle
Tél: (450)-318-5907
Courriel: vorelli.mnt@brastomail.com

Font styles to use
Sans Serif

Colors
f78f20
0455a3

Requirements
Must have
• My company name: VORELLI Maintenance Industrielle My phone: (450) -318-5907 My email: vorelli.mnt@brastomail.com
Nice to have
• Integrate a representative logo of the mechanics (gears, mechanical parts)

```html
<!DOCTYPE html>
<html lang="fr">
<head>
<meta charset="utf-8">
<title>VORELLI Maintenance Industrielle – Cartes d'affaires</title>
<link href="https://fonts.googleapis.com/css2?family=Lato:wght@400;700&display=swap" rel="stylesheet">
<style>
  :root {
    --stage: #3a3431;
    --card: #0b0b0c;
    --brand-blue: #1f6fc9;
    --silver: #c9c9c9;
    --text-light: #e6e6e6;
    --divider: #3b3b3d;
  }
  * { box-sizing: border-box; margin: 0; padding: 0; }
  html, body {
    width: 1200px; height: 900px; overflow: hidden;
    background: var(--stage);
    font-family: "Lato", Arial, sans-serif;
  }
  .stage {
    width: 1200px; height: 900px;
    display: flex; align-items: center; justify-content: center; gap: 60px;
  }
  .card {
    width: 525px; height: 300px;
    background: var(--card);
    border-radius: 3px;
    box-shadow: 0 14px 30px rgba(0,0,0,.45);
    position: relative;
  }
  /* Front face */
  .card-front { display: flex; }
  .brand-panel {
    width: 290px; height: 100%;
    display: flex; flex-direction: column; align-items: center; justify-content: center; gap: 14px;
    border-right: 1px solid var(--divider);
  }
  .brand-mark {
    width: 46px; height: 46px; border-radius: 50%;
    background: var(--brand-blue);
  }
  .brand-name {
    font-weight: 700; text-align: center; line-height: 1.05;
    color: var(--brand-blue); letter-spacing: 3px;
  }
  .brand-name .word { display: block; font-size: 50px; }
  .brand-name .tagline { display: block; font-size: 14px; letter-spacing: 1px; margin-top: 6px; }
  .contact-panel {
    flex: 1; padding: 58px 0 0 26px;
    color: var(--text-light);
  }
  .person-name { color: var(--brand-blue); font-size: 17px; font-weight: 400; letter-spacing: .5px; }
  .person-role { font-size: 15px; margin-top: 2px; }
  .contact-list { list-style: none; margin-top: 26px; font-size: 14px; }
  .contact-list li { display: flex; align-items: center; gap: 7px; margin-bottom: 5px; }
  .contact-list svg { width: 11px; height: 11px; fill: var(--brand-blue); flex: none; }
  /* Back face */
  .card-back {
    display: flex; flex-direction: column; align-items: center; justify-content: center; gap: 16px;
  }
  .card-back .brand-mark { background: var(--silver); width: 56px; height: 56px; }
  .card-back .brand-name { color: var(--silver); }
  .card-back .brand-name .word { font-size: 56px; }
  .card-back .brand-name .tagline { font-size: 15px; }
</style>
</head>
<body>
<main class="stage">
  <section class="card card-front" aria-label="Recto de la carte">
    <div class="brand-panel">
      <span class="brand-mark" aria-hidden="true"></span>
      <h1 class="brand-name"><span class="word">VORELLI</span><span class="tagline">MAINTENANCE INDUSTRIELLE</span></h1>
    </div>
    <div class="contact-panel">
      <p class="person-name">JULIEN MARCHAND</p>
      <p class="person-role">Managing Director</p>
      <ul class="contact-list">
        <li><svg viewBox="0 0 24 24" aria-hidden="true"><path d="M6.6 10.8a15 15 0 0 0 6.6 6.6l2.2-2.2c.3-.3.7-.4 1-.2 1.1.4 2.3.6 3.6.6.6 0 1 .4 1 1V20c0 .6-.4 1-1 1C10.6 21 3 13.4 3 4c0-.6.4-1 1-1h3.5c.6 0 1 .4 1 1 0 1.3.2 2.5.6 3.6.1.3 0 .7-.2 1z"/></svg>(450) -318-5907</li>
        <li><svg viewBox="0 0 24 24" aria-hidden="true"><path d="M2 5h20v14H2zm2 2v.5l8 5 8-5V7l-8 5z"/></svg>vorelli.mnt@brastomail.com</li>
      </ul>
    </div>
  </section>
  <section class="card card-back" aria-label="Verso de la carte">
    <span class="brand-mark" aria-hidden="true"></span>
    <p class="brand-name"><span class="word">VORELLI</span><span class="tagline">MAINTENANCE INDUSTRIELLE</span></p>
  </section>
</main>
</body>
</html>
```